2 guided dives on the North of Bonaire

2 guided shore dives on the North of Bonaire including authentic local lunch and drinks.
We offer an adventure for experienced divers to discover the dive sites on the north of the island.
Showing you the beauty of the reefs and tasting authentic local cuisine like goat or iguana combined with a stunning view of the surroundings.

Target Market(s)

Divers / tourism

Industry/Entity Type

Tourism / Diving

Font styles to use
Sans Serif

Colors
0054AA
0677BA
7BADD7
CADEEF
E8F1F8
0094D4
00A9DD
6FCCEA
C7EBF8
E9F6FB
F0912C
F2A743
F7CA91
FBE8D2
FDF5EE
EE7325
F08F49
F5BC92
FAE3D3
FDF4ED

Requirements
Must have
• Some of the pictures I uploaded and the food picture / bottom like in the pictures
Nice to have
• inviting to join us on the guided dives
Should not have
• Any picture I didn't provide

```html
<!DOCTYPE html>
<html lang="en">
<head>
<meta charset="utf-8">
<title>Let Us Guide You – Guided Dives Flyer</title>
<link rel="stylesheet" href="https://fonts.googleapis.com/css2?family=Poppins:ital,wght@0,500;0,600;0,700;0,800;1,800;1,900&display=swap">
<style>
  :root{
    --navy:#0b2a55;
    --deep-blue:#0054AA;
    --blue:#0677BA;
    --sky:#0094D4;
    --cyan:#00A9DD;
    --light-cyan:#6FCCEA;
    --pale-blue:#E8F1F8;
    --orange:#F0912C;
    --dark-orange:#EE7325;
    --gold:#F2A743;
    --white:#ffffff;
    --ink:#1d2b40;
  }
  *{box-sizing:border-box;margin:0;padding:0}
  html,body{width:766px;height:1200px;overflow:hidden;background:var(--white)}
  body{font-family:"Poppins",Arial,sans-serif;color:var(--ink)}
  .flyer{position:relative;width:766px;height:1200px;background:var(--white);overflow:hidden}

  .hero{position:absolute;left:0;top:0;width:766px;height:470px}
  .brand{position:absolute;left:28px;top:22px;display:flex;align-items:center;gap:8px;
    background:var(--white);padding:8px 14px;border-radius:6px}
  .brand__dot{width:22px;height:22px;border-radius:50%;background:var(--orange)}
  .brand__name{font-weight:800;font-size:17px;color:var(--deep-blue);letter-spacing:.2px}

  .headline{position:absolute;left:0;width:100%;top:478px;text-align:center;
    font-weight:900;font-style:italic;font-size:64px;line-height:1;color:var(--deep-blue);
    letter-spacing:.5px}
  .offer{position:absolute;left:70px;top:566px}
  .offer__title{display:flex;align-items:center;gap:12px;font-weight:800;font-size:21px;color:var(--navy)}
  .offer__icon{width:26px;height:26px;background:var(--orange);border-radius:4px}
  .offer__list{list-style:none;margin:12px 0 0 6px}
  .offer__list li{display:flex;align-items:center;gap:10px;font-weight:600;font-size:16px;color:var(--ink);margin-bottom:6px}
  .offer__list svg{flex:none}

  .lunch-band{position:absolute;left:0;top:676px;width:100%;height:44px;background:var(--sky);
    color:var(--white);font-weight:800;font-size:18px;text-align:center;line-height:44px;letter-spacing:.3px}

  .food{position:absolute;left:0;top:720px;width:766px;height:330px}
  .invite{position:absolute;right:44px;top:850px;text-align:right;font-weight:800;
    font-size:30px;line-height:1.15;color:var(--deep-blue)}
  .invite__accent{color:var(--orange);font-style:italic;text-decoration:underline;text-decoration-thickness:3px;text-underline-offset:5px}

  .footer{position:absolute;left:0;bottom:0;width:100%;height:150px;background:var(--navy);
    border-top:8px solid var(--cyan);display:flex;align-items:center;padding:0 30px;gap:24px}
  .footer .brand{position:static}
  .contacts{display:grid;grid-template-columns:1fr 1fr;gap:10px 12px;flex:1}
  .contact{display:flex;align-items:center;gap:8px;background:var(--orange);color:var(--white);
    font-weight:700;font-size:14px;padding:7px 12px;border-radius:4px}
  .badge{width:78px;height:78px;border-radius:50%;background:var(--white);flex:none}
</style>
</head>
<body>
<main class="flyer">

  <svg class="hero" viewBox="0 0 766 470" aria-hidden="false">
    <defs>
      <linearGradient id="beach" x1="0" y1="0" x2="1" y2="1">
        <stop offset="0" stop-color="#6FCCEA"/><stop offset=".55" stop-color="#00A9DD"/><stop offset="1" stop-color="#e9dcc0"/>
      </linearGradient>
      <linearGradient id="coast" x1="0" y1="0" x2="0" y2="1">
        <stop offset="0" stop-color="#7BADD7"/><stop offset=".5" stop-color="#0677BA"/><stop offset="1" stop-color="#5c6b52"/>
      </linearGradient>
      <linearGradient id="shore" x1="0" y1="0" x2="1" y2="0">
        <stop offset="0" stop-color="#0094D4"/><stop offset="1" stop-color="#C7EBF8"/>
      </linearGradient>
    </defs>
    <rect width="766" height="470" fill="#0b2a55"/>
    <polygon points="0,0 520,0 250,470 0,470" fill="#0054AA"/>
    <polygon role="img" aria-label="Photo of a white beach along turquoise water" points="140,0 766,0 766,300 400,470 60,470" fill="url(#beach)" stroke="#fff" stroke-width="8"/>
    <polygon role="img" aria-label="Photo of the rocky north coast under blue sky" points="0,120 190,40 300,470 0,470" fill="url(#coast)" stroke="#fff" stroke-width="8"/>
    <polygon role="img" aria-label="Photo of shallow reef water near the shore" points="560,250 766,150 766,470 470,470" fill="url(#shore)" stroke="#fff" stroke-width="8"/>
    <polygon points="0,440 766,400 766,470 0,470" fill="#fff"/>
  </svg>

  <div class="brand">
    <span class="brand__dot"></span><span class="brand__name">Northshore Dive</span>
  </div>

  <h1 class="headline">LET US GUIDE YOU!</h1>

  <section class="offer">
    <h2 class="offer__title"><span class="offer__icon"></span>GUIDED DIVES AT THE NORTH SIDE OF BONAIRE</h2>
    <ul class="offer__list">
      <li><svg width="18" height="18" viewBox="0 0 18 18"><rect width="18" height="18" rx="3" fill="#F0912C"/><path d="M4 9.5l3.2 3L14 5.5" stroke="#fff" stroke-width="2.4" fill="none"/></svg>You just enjoy the dives, we take care of the rest</li>
      <li><svg width="18" height="18" viewBox="0 0 18 18"><rect width="18" height="18" rx="3" fill="#F0912C"/><path d="M4 9.5l3.2 3L14 5.5" stroke="#fff" stroke-width="2.4" fill="none"/></svg>We show you the cool stuff</li>
    </ul>
  </section>

  <div class="lunch-band">AUTHENTIC LOCAL LUNCH AND DRINKS AT POSADA VISTA ALTA</div>

  <svg class="food" viewBox="0 0 766 330">
    <defs>
      <linearGradient id="meal" x1="0" y1="0" x2="1" y2="1">
        <stop offset="0" stop-color="#F7CA91"/><stop offset=".45" stop-color="#c8742d"/><stop offset="1" stop-color="#6b3a1c"/>
      </linearGradient>
    </defs>
    <polygon points="0,0 470,0 420,330 0,330" fill="#E9F6FB"/>
    <polygon role="img" aria-label="Photo of a local plate with stewed goat, rice and fried plantain" points="0,0 400,0 330,165 400,330 0,330" fill="url(#meal)" stroke="#fff" stroke-width="6"/>
    <polygon points="400,0 430,0 360,165 430,330 400,330 330,165" fill="#0094D4"/>
  </svg>

  <p class="invite">JOIN US ON THE<br><span class="invite__accent">GUIDED DIVES</span></p>

  <footer class="footer">
    <div class="brand"><span class="brand__dot"></span><span class="brand__name">Northshore Dive</span></div>
    <div class="contacts">
      <span class="contact"><svg width="14" height="14" viewBox="0 0 24 24"><path d="M6.6 10.8a15 15 0 006.6 6.6l2.2-2.2c.3-.3.7-.4 1-.2 1.1.4 2.3.6 3.6.6.6 0 1 .4 1 1V20c0 .6-.4 1-1 1A17 17 0 013 4c0-.6.4-1 1-1h3.5c.6 0 1 .4 1 1 0 1.3.2 2.5.6 3.6.1.3 0 .7-.2 1z" fill="#fff"/></svg>+599 700 1234</span>
      <span class="contact"><svg width="14" height="14" viewBox="0 0 24 24"><path d="M6.6 10.8a15 15 0 006.6 6.6l2.2-2.2c.3-.3.7-.4 1-.2 1.1.4 2.3.6 3.6.6.6 0 1 .4 1 1V20c0 .6-.4 1-1 1A17 17 0 013 4c0-.6.4-1 1-1h3.5c.6 0 1 .4 1 1 0 1.3.2 2.5.6 3.6.1.3 0 .7-.2 1z" fill="#fff"/></svg>+599 700 5678</span>
      <span class="contact">info@northshoredive.com</span>
      <span class="contact">northshoredive.com</span>
    </div>
    <div class="badge" role="img" aria-label="Dive certification badge"></div>
  </footer>

</main>
</body>
</html>
```